Brochure for financial planning firm

I need a brochure designed that will be folded into three panels idealy. I will provide the copy, logo, and some of the pictures.

Our primary business is finding investors for large-scale real estate developments.

Some of the pictures will have to come from outside this website given the file sizes. Please click the following link to download pictures of projects we have raised money for:

https://files.plorvex.net/share/7Qm2KtLw9ZxR4nVbY8HcPdJ3sFgT

Target Market(s)

People Ages 30 to 75. That are unsatisfied with their retirement investments

Industry/Entity Type

Financial

Requirements
Must have
• Addition to copy:
• To recieve information on our latest investments visit www.growsteadyfunds.ca
• Contact info:
• Torvanek Wealth Management Inc.
• 7 Orchard St. W.
• Suite K240
• Hamilton, ON L2P 5R8
• Office: (905) 634-2918
• www.torvanekwm.com
• The brochure must have somewhere printed on it near our contact info: RBTQ Lic # 40561

```html
<!DOCTYPE html>
<html lang="en">
<head>
<meta charset="utf-8">
<title>Syndicated Mortgages Brochure</title>
<link rel="stylesheet" href="https://fonts.googleapis.com/css2?family=Tinos:ital,wght@0,400;0,700;1,400;1,700&display=swap">
<style>
  :root {
    --page-bg: #e6e7e9;
    --navy-top: #2d2b3b;
    --navy-bottom: #1c1a26;
    --teal: #2b9a86;
    --teal-dark: #1f7a6a;
    --paper: #f6f6f4;
    --paper-shade: #ecedeb;
    --ink: #2c2c30;
    --white: #ffffff;
    --brick: #8a6a55;
    --sky: #8fb0c8;
    --foliage: #6d7d4a;
  }
  * { box-sizing: border-box; margin: 0; padding: 0; }
  html, body {
    width: 1200px; height: 1000px; overflow: hidden;
    background: var(--page-bg);
    font-family: "Tinos", "Times New Roman", serif;
    color: var(--ink);
  }
  .brochure {
    position: absolute; left: 45px; top: 60px;
    width: 1110px; height: 880px;
    box-shadow: 0 10px 30px rgba(0,0,0,.18);
    overflow: hidden;
  }
  .panel {
    position: absolute; top: 0; width: 370px; height: 880px;
  }
  .panel--intro {
    left: 0;
    background: linear-gradient(180deg, var(--navy-top), var(--navy-bottom));
    color: var(--white);
    padding: 44px 30px 0 30px;
  }
  .panel--benefits { left: 370px; background: var(--paper); }
  .panel--testimonials {
    left: 740px; background: linear-gradient(180deg, var(--paper), var(--paper-shade));
    padding: 38px 28px 0 28px;
  }
  .panel-title {
    font-size: 27px; font-weight: 700; letter-spacing: 1px; line-height: 1.05;
    text-transform: uppercase; margin-bottom: 16px;
  }
  .panel-title .accent { color: var(--teal); display: block; }
  .panel--intro p { font-size: 12.6px; line-height: 1.38; margin-bottom: 11px; }
  .pull-quote {
    margin-top: 22px; font-style: italic; font-size: 13px; line-height: 1.42;
  }
  .pull-quote cite {
    display: block; font-style: normal; font-weight: 700; margin-top: 8px;
  }
  .hero-photo {
    height: 250px;
    background: linear-gradient(160deg, var(--sky) 0%, #b7a393 28%, var(--brick) 55%, #5d4a3f 80%, var(--foliage) 100%);
  }
  .benefits-body { padding: 30px 30px 0 30px; }
  .benefits-intro { font-size: 12.8px; line-height: 1.4; margin-bottom: 16px; }
  .benefit { display: flex; gap: 10px; margin-bottom: 16px; }
  .benefit-icon { flex: 0 0 20px; margin-top: 14px; }
  .benefit-title {
    font-size: 14px; font-weight: 700; text-transform: uppercase; letter-spacing: .3px;
  }
  .benefit-title .accent { color: var(--teal); }
  .benefit p { font-size: 12.6px; line-height: 1.36; }
  .section-title {
    font-size: 24px; font-weight: 700; letter-spacing: 1px; text-transform: uppercase;
    margin-bottom: 10px;
  }
  .testimonial { margin-bottom: 11px; }
  .testimonial p { font-size: 11.4px; line-height: 1.34; }
  .testimonial .author {
    display: block; font-size: 11.6px; font-weight: 700; font-style: italic; margin-top: 5px;
  }
  .street-photo {
    position: absolute; left: 0; bottom: 0; width: 1110px; height: 170px;
    background: linear-gradient(90deg, #6b5546 0%, #a8876b 20%, #c7b39a 38%, #7d8a5c 55%, #b49a80 72%, #6f7f55 88%, #8b7360 100%);
  }
  .teal-sweep {
    position: absolute; left: 0; bottom: 150px; width: 1110px; height: 60px;
  }
</style>
</head>
<body>
<main class="brochure">

  <section class="panel panel--intro">
    <h1 class="panel-title">Syndicated <span class="accent">Mortgages</span></h1>
    <p>The simplest way to describe a syndicated mortgage is that it is a mortgage where two or more people loan their money in the form of one mortgage to another party.</p>
    <p>As a syndicated mortgage investor you become the bank! In other words, when you invest in a syndicated mortgage offered by Torvanek Wealth Management you are lending your money to a reputable real estate developer for a set interest rate.</p>
    <p>You might be thinking that lending mortgages are only for people with really deep pockets but in fact, if you have even $25,000 sitting in an account a mortgage investment is something you could take advantage of. RRSP, TFSA, RRIF, LIRA’s, and LIF’s are only some of the account types that are eligible for syndicated mortgage investments.</p>
    <blockquote class="pull-quote">
      “Mortgage investments are quickly changing retirement portfolios. People are tired of not having control over their money. The uncertainty of the markets keeps people up at night. As a financial planner mortgage investments give my clients and I a more stable position to plan their financial lives from.”
      <cite>– Dario M. Castell, Principal Broker at Torvanek Wealth Management</cite>
    </blockquote>
  </section>

  <section class="panel panel--benefits">
    <div class="hero-photo" role="img" aria-label="Photo of a modern brick apartment building with glass balconies"></div>
    <div class="benefits-body">
      <p class="benefits-intro">There are many reasons why banks use mortgages as their preferred investments, here are just a few of those reasons and why you might want to think about adding a syndicated mortgage investment to your portfolio:</p>

      <div class="benefit">
        <svg class="benefit-icon" width="20" height="20" viewBox="0 0 20 20" aria-hidden="true"><circle cx="10" cy="10" r="10" fill="var(--teal)"/><path d="M5.5 10.3l3 3 6-6.3" fill="none" stroke="#fff" stroke-width="2.2" stroke-linecap="round" stroke-linejoin="round"/></svg>
        <div>
          <h3 class="benefit-title">Security <span class="accent">of Principle</span></h3>
          <p>Your investment is registered against physical real estate at the Land Registry Office. This doesn’t mean it’s a guaranteed investment, but it definitely reduces the risk of loss! No mutual fund or stock portfolio can do that.</p>
        </div>
      </div>

      <div class="benefit">
        <svg class="benefit-icon" width="20" height="20" viewBox="0 0 20 20" aria-hidden="true"><circle cx="10" cy="10" r="10" fill="var(--teal)"/><path d="M5.5 10.3l3 3 6-6.3" fill="none" stroke="#fff" stroke-width="2.2" stroke-linecap="round" stroke-linejoin="round"/></svg>
        <div>
          <h3 class="benefit-title">A Predictable <span class="accent">Rate of Return</span></h3>
          <p>With a syndicated mortgage investment you know exactly what you are entitled to earn from your investment because your rate of interest is written right into your contract with the borrower. No more ups and downs of the stock market.</p>
        </div>
      </div>

      <div class="benefit">
        <svg class="benefit-icon" width="20" height="20" viewBox="0 0 20 20" aria-hidden="true"><circle cx="10" cy="10" r="10" fill="var(--teal)"/><path d="M5.5 10.3l3 3 6-6.3" fill="none" stroke="#fff" stroke-width="2.2" stroke-linecap="round" stroke-linejoin="round"/></svg>
        <div>
          <h3 class="benefit-title">Term <span class="accent">Investment Periods</span></h3>
          <p>A syndicated mortgage investment can range between a few months to about five years, depending on the project being built.</p>
        </div>
      </div>
    </div>
  </section>

  <section class="panel panel--testimonials">
    <h2 class="section-title">Testimonials</h2>
    <div class="testimonial">
      <p>My husband and I had been looking for an alternative to investing in mutual funds and the stock market for a while. The unpredictability of our mutual funds was something we were sick and tired of. When we were introduced to the syndicated mortgage investments offered by Torvanek Wealth Management, I thought the rate of return was too good to be true, that is until we attended one of their introductory seminars. Now that we invested some of our money with Torvanek I don’t cringe when my investment statements come in the mail, and we can sleep at night.</p>
      <span class="author">Marina Velloso, Client</span>
    </div>
    <div class="testimonial">
      <p>Dario took the time to meet with us, he helped organize our current assets and then helped us to focus on our future needs and goals. He was very knowledgeable of all products and explained everything to us in non-technical terms. We now feel more comfortable with our portfolio and are confident that Dario will help us achieve financial success and growth. I would definitely recommend Dario to any of my family or friends.</p>
      <span class="author">Renata Olsberg, CA</span>
    </div>
    <div class="testimonial">
      <p>When you are looking to expand your investment and real estate portfolio, Torvanek Wealth Management Inc is a true asset. I have gotten to know Dario Castell (Principal Broker at Torvanek Wealth Management) over the years, and he always demonstrates a keen knowledge and creative edge.</p>
      <span class="author">Owen Harlick, Professional Real Estate Investor</span>
    </div>
    <div class="testimonial">
      <p>I would recommend Torvanek Wealth Management (TWM) to anyone looking for professional financial advice regarding real estate investment strategy, and/or financial planning. With the experience and expertise of the TWM team, they can tailor solutions for their clients through a variety of products ranging from the traditional financial services to alternative investments such as syndicated mortgages and private mortgage lending. In addition, the TWM team is reliable, trustworthy, and focused on helping their clients achieve their financial goals.</p>
      <span class="author">Felix Draymore,<br>Winner of the 2017 Rising Star award by Northern Property Ledger Magazine</span>
    </div>
  </section>

  <div class="street-photo" role="img" aria-label="Photo of a tree-lined street of brick townhouses"></div>
  <svg class="teal-sweep" viewBox="0 0 1110 60" preserveAspectRatio="none" aria-hidden="true">
    <path d="M0 0 H370 V8 C500 40 620 40 740 22 C850 8 980 4 1110 14 V60 H0 Z" fill="var(--teal)"/>
    <path d="M0 0 C120 18 250 22 370 8 V0 Z" fill="var(--navy-bottom)"/>
    <path d="M0 0 C120 18 250 22 370 8 C500 40 620 40 740 22 C850 8 980 4 1110 14 V24 C980 16 850 22 740 36 C620 52 500 52 370 22 C250 36 120 34 0 18 Z" fill="var(--teal-dark)" opacity=".55"/>
  </svg>

</main>
</body>
</html>
```